Vertical Design 11.5"x 84"

this project is going to be 12 different design panels that will go in our retail store, Trelvan Security Doors. These designs will be 11.5" x 84" and will be displayed with our doors. https://trelvansecuritydoors.example/
There are 12 places in our door displays to put these graphics. See our photo demonstrating where the graphics will go.
Ideas for the graphics:
1. image backgrounds can be brick, vinyl siding, split shake siding, in various colors and styles, sunny day, flowery grassy meadow, use your imagination.
2. graphics can be words and phrases like - Made In The USA, Custom Sizes,
3. Images used can be entry doors side-lites, security side-lites (see photo of door with 2 security side lites)
All these graphics are about entry doors, security doors, and patio doors.
Use vibrant colors, things that are exciting. There's 12 different panels so use your creativity to mix it up.
You can use the bee guy theme that was created in the past that would be great to add continuity to our marketing.
Target Market(s)
HOME OWNERS
Look and feel
Each slider illustrates characteristics of the customer's brand and the style your logo design should communicate.

```html
<!DOCTYPE html>
<html lang="en">
<head>
<meta charset="utf-8">
<title>Trelvan Security Doors – Vertical Display Panels</title>
<link href="https://fonts.googleapis.com/css2?family=Montserrat:wght@500;700&display=swap" rel="stylesheet">
<style>
  :root{
    --page:#ffffff;
    --brick-light:#d9844a;
    --brick-mid:#c8663a;
    --brick-dark:#a8522e;
    --mortar:#cfc6b8;
    --leaf-dark:#1f2e29;
    --leaf-mid:#3f6250;
    --leaf-light:#5e8a70;
    --window-grey:#6f7a82;
    --window-sky:#a9b6c0;
    --window-frame:#e6eaee;
    --blossom:#eef0ee;
    --sky-pale:#d4f1fb;
    --tower-pink:#c98a78;
    --tower-shade:#a96a5b;
    --text-white:#ffffff;
    --text-black:#0d0d0d;
    --text-gold:#f2cf62;
  }
  *{margin:0;padding:0;box-sizing:border-box}
  html,body{width:1200px;height:1032px;overflow:hidden;background:var(--page)}
  .canvas{position:relative;width:1200px;height:1032px;font-family:"Montserrat",sans-serif}
  .panel{position:absolute;top:137px;width:105px;height:765px;overflow:hidden}
  .photo{position:absolute;inset:0}
  .photo--brick{
    background:
      repeating-linear-gradient(180deg, transparent 0 58px, var(--mortar) 58px 62px),
      linear-gradient(180deg, var(--brick-light), var(--brick-mid) 45%, var(--brick-light) 70%, var(--brick-dark));
  }
  .photo--leaves{
    background:
      radial-gradient(circle at 30% 20%, var(--leaf-light), transparent 40%),
      radial-gradient(circle at 70% 65%, var(--leaf-light), transparent 45%),
      linear-gradient(180deg, var(--leaf-mid), var(--leaf-dark) 50%, var(--leaf-mid));
  }
  .photo--window{
    background:
      linear-gradient(180deg, transparent 0 70%, var(--blossom) 82%, #8a8070 100%),
      linear-gradient(90deg, var(--window-grey), var(--window-sky) 50%, var(--window-grey));
  }
  .photo--tower{
    background:
      linear-gradient(168deg, var(--sky-pale) 0 47%, var(--tower-pink) 47.2% 100%);
  }
  .photo--tower::after{
    content:"";position:absolute;right:0;top:45%;bottom:0;width:40%;
    background:linear-gradient(180deg,var(--tower-shade),var(--tower-pink));
  }
  .slogan{
    position:absolute;top:146px;left:50%;transform:translateX(-50%);
    writing-mode:vertical-rl;font-size:57px;line-height:1;white-space:nowrap;letter-spacing:0.5px;
  }
  .slogan .strong{font-weight:700}
  .slogan .light{font-weight:500}
  .slogan--white{color:var(--text-white)}
  .slogan--black{color:var(--text-black)}
  .word--gold{color:var(--text-gold)}
  .word--black{color:var(--text-black)}
  .word--white{color:var(--text-white)}
  .brandmark{
    position:absolute;top:320px;left:50%;transform:translateX(-50%);
    display:flex;flex-direction:column;align-items:center;gap:8px;
  }
  .brandmark__dot{width:18px;height:18px;border-radius:50%;background:var(--text-white)}
  .brandmark__name{
    writing-mode:vertical-rl;color:var(--text-white);font-weight:700;font-size:15px;
    letter-spacing:2px;white-space:nowrap;
  }
</style>
</head>
<body>
<main class="canvas">

  <section class="panel" style="left:49px">
    <div class="photo photo--brick" role="img" aria-label="Orange brick wall photo"></div>
    <p class="slogan slogan--white strong">CUSTOM SIZES</p>
  </section>

  <section class="panel" style="left:174px">
    <div class="photo photo--leaves" role="img" aria-label="Green leafy foliage photo"></div>
    <div class="brandmark"><span class="brandmark__dot"></span><span class="brandmark__name">TRELVAN SECURITY DOORS</span></div>
  </section>

  <section class="panel" style="left:300px">
    <div class="photo photo--window" role="img" aria-label="White window frame with flowers below"></div>
  </section>

  <section class="panel" style="left:425px">
    <div class="photo photo--brick" role="img" aria-label="Orange brick wall photo"></div>
    <p class="slogan slogan--black strong">CUSTOM SIZES</p>
  </section>

  <section class="panel" style="left:553px">
    <div class="photo photo--leaves" role="img" aria-label="Green leafy foliage photo"></div>
    <div class="brandmark"><span class="brandmark__dot"></span><span class="brandmark__name">TRELVAN SECURITY DOORS</span></div>
  </section>

  <section class="panel" style="left:678px">
    <div class="photo photo--tower" role="img" aria-label="Pink brick building corner against pale sky"></div>
    <p class="slogan"><span class="light word--gold">MADE </span><span class="strong word--black">IN USA</span></p>
  </section>

  <section class="panel" style="left:801px">
    <div class="photo photo--brick" role="img" aria-label="Orange brick wall photo"></div>
  </section>

  <section class="panel" style="left:922px">
    <div class="photo photo--leaves" role="img" aria-label="Green leafy foliage photo"></div>
    <div class="brandmark"><span class="brandmark__dot"></span><span class="brandmark__name">TRELVAN SECURITY DOORS</span></div>
  </section>

  <section class="panel" style="left:1046px">
    <div class="photo photo--window" role="img" aria-label="White window frame with flowers below"></div>
    <p class="slogan"><span class="light word--white">MADE </span><span class="strong word--gold">IN USA</span></p>
  </section>

</main>
</body>
</html>
```